Bremoda brochure 2014

Bremoda Australia was the first company to introduce retractable fly screens in Australia (about 30 years ago). At present, Bremoda is a designer and manufacturer of retractable and pleated fly screens. 100% Australian made and owned.

The use of retractable fly screens has always been related to the Australian style of living: open spaces to the views and fresh air. Now more than ever, with the new technologies and designs in windows and doors, the living areas are opening more and more and is very common to find houses with very big openings where bifold or stacker doors are installed.

There are now many manufacturers and importers. However the high quality remain within the local manufacturers.

Our requirement is the design of 1 brochure for our range of products.
Sizes / designs are open to two formats:
1. DL size brochure (A4 tri-fold)
2. A5 (A4 folded in half).
Copy, photos, logo and our design elements are provided.
Previous brochure is also provided as an example (not the best "does the job" but could be much better).
The brochure is intended for our resellers they handout the brochure to their prospective clients. It will also be available in our website to download as pdf.

Target Market(s)

Our target market can be described as "owners of beautiful houses".
Houses with stunning views and beautiful openings. Women are often the decision makers and they want a discreet and elegant addition to their doors.

Industry/Entity Type

It Company

Font styles to use
Sans Serif
Other font styles liked:
• Suggested: Hevetica Neue or Source Sans Pro (used in our website).

Requirements
Must have
• We have a graphic element we call "the wave". We like it and it is present in all we do.
The use of it should be limited (not too much) but it must be present.

```html
<!DOCTYPE html>
<html lang="en">
<head>
<meta charset="utf-8">
<title>Bremoda brochure 2014</title>
<link rel="stylesheet" href="https://fonts.googleapis.com/css2?family=Source+Sans+3:wght@300;400;600;700&display=swap">
<style>
  :root {
    --page-bg: #e6e6e6;
    --paper: #ffffff;
    --sand: #efece7;
    --brown: #6e5a3e;
    --brown-text: #7a6446;
    --orange: #e8914a;
    --label-band: rgba(255,255,255,0.82);
    --sea: #8fb0c8;
    --terrace: #a89a86;
    --timber: #b98a4c;
    --map: #ece9e5;
  }
  * { box-sizing: border-box; margin: 0; padding: 0; }
  html, body { width: 1200px; height: 1000px; overflow: hidden; }
  body {
    background: var(--page-bg);
    font-family: "Source Sans 3", "Helvetica Neue", Arial, sans-serif;
    position: relative;
  }
  .brochure {
    position: absolute; left: 203px; top: 198px;
    width: 842px; height: 597px;
    background: var(--paper);
    overflow: hidden;
  }
  .photo { position: absolute; }
  .photo-harbour { left: 0; top: 0; width: 281px; height: 125px;
    background: linear-gradient(180deg, #a9c8e4 0%, #7f9a86 35%, var(--sea) 55%, #b8c9d2 100%); }
  .photo-balcony { left: 281px; top: 0; width: 281px; height: 125px;
    background: linear-gradient(90deg, #b9c9d3 0%, #c9c4b8 25%, #8a8a88 45%, #3d3b39 60%, #8d7f70 80%, var(--terrace) 100%); }
  .photo-french-door { left: 562px; top: 0; width: 280px; height: 430px;
    background: linear-gradient(180deg, #cfc6b4 0%, #9f9482 30%, #6e6658 55%, #b3a58d 80%, #d8ccb6 100%); }
  .photo-sliding-door { left: 0; top: 447px; width: 281px; height: 150px;
    background: linear-gradient(90deg, #5b6e3c 0%, var(--timber) 20%, #3b3430 45%, #c6b8a2 65%, #8b4a36 90%, #4f6e3a 100%); }

  .label {
    position: absolute; top: 125px; height: 27px; width: 281px;
    background: var(--label-band);
    color: var(--brown); font-size: 19px; font-weight: 400;
    text-align: center; line-height: 27px;
  }
  .label-1 { left: 0; } .label-2 { left: 281px; } .label-3 { left: 562px; width: 280px; }

  .intro-panel { position: absolute; left: 0; top: 152px; width: 281px; height: 270px; background: var(--sand); }
  .brace { position: absolute; left: 20px; top: 40px; color: #fff; font-size: 150px; font-weight: 300; line-height: 1; }
  .intro-text { position: absolute; left: 77px; top: 96px; width: 190px;
    color: var(--brown-text); font-size: 16px; line-height: 20px; font-weight: 400; }

  .features { position: absolute; left: 323px; top: 178px; width: 210px;
    color: var(--brown-text); font-size: 10px; line-height: 12px; font-weight: 400; }
  .features p { margin-bottom: 12px; }
  .features ul { list-style: none; }
  .features li { font-weight: 700; font-size: 11.5px; line-height: 14.4px; }
  .features li::before { content: "•"; color: var(--orange); margin-right: 5px; font-weight: 400; }

  .wave { position: absolute; left: 0; top: 405px; width: 842px; height: 45px; }

  .fold-shade { position: absolute; top: 447px; height: 150px; }
  .fold-2 { left: 281px; width: 281px; background: linear-gradient(90deg, #e8e8e8 0%, #fff 35%, #fff 75%, #eee 100%); }
  .fold-3 { left: 562px; width: 280px; background: linear-gradient(90deg, #ececec 0%, #fff 30%); }

  .years-map { position: absolute; left: 368px; top: 470px; width: 112px; height: 105px;
    background: var(--map); border-radius: 40% 45% 35% 30%; }
  .years { position: absolute; left: 368px; top: 492px; width: 105px; text-align: center;
    color: #fff; font-weight: 700; }
  .years strong { display: block; font-size: 20px; line-height: 20px; }
  .years span { display: block; font-size: 11px; line-height: 12px; }

  .history { position: absolute; left: 587px; top: 481px; width: 225px;
    color: var(--brown-text); font-size: 12px; line-height: 15px; }
</style>
</head>
<body>
  <main class="brochure">
    <div class="photo photo-harbour" role="img" aria-label="Balcony with glass balustrade overlooking a harbour with moored yachts"></div>
    <div class="photo photo-balcony" role="img" aria-label="Open glass door onto a timber balcony"></div>
    <div class="photo photo-french-door" role="img" aria-label="Open French doors onto an ornate wrought iron balcony"></div>

    <h2 class="label label-1">Discreet</h2>
    <h2 class="label label-2">Stylish</h2>
    <h2 class="label label-3">Rewarding</h2>

    <section class="intro-panel">
      <div class="brace" aria-hidden="true">}</div>
      <p class="intro-text">An Bremoda screen will help you get the most of your beautiful doors and openings.</p>
    </section>

    <section class="features">
      <p>What is the point of having beautiful doors and openings if you can't really use them?</p>
      <p>Our fly screen solutions are designed to blend in with the door frames and respect your home. It is all about looks and functionality coupled in perfect balance.</p>
      <p>We have solutions for:</p>
      <ul>
        <li>Bifold doors</li>
        <li>French doors</li>
        <li>Stacker doors</li>
        <li>Hinged and sliding doors</li>
        <li>Windows</li>
        <li>Verandas</li>
        <li>Large openings</li>
        <li>Difficult to screen openings</li>
      </ul>
    </section>

    <div class="fold-shade fold-2"></div>
    <div class="fold-shade fold-3"></div>

    <svg class="wave" viewBox="0 0 842 45" preserveAspectRatio="none" aria-hidden="true">
      <defs>
        <linearGradient id="waveFill" x1="0" x2="1" y1="0" y2="0">
          <stop offset="0" stop-color="#a9d3ec"/>
          <stop offset="0.35" stop-color="#dfe7ea"/>
          <stop offset="0.6" stop-color="#f1e0cd"/>
          <stop offset="1" stop-color="#f0a25c"/>
        </linearGradient>
        <linearGradient id="waveLine" x1="0" x2="1" y1="0" y2="0">
          <stop offset="0" stop-color="#6fb5dc"/>
          <stop offset="0.45" stop-color="#b08a5c"/>
          <stop offset="1" stop-color="#e27f2e"/>
        </linearGradient>
      </defs>
      <path d="M0 2 C200 20 500 38 842 6 L842 42 L0 42 Z" fill="url(#waveFill)"/>
      <path d="M0 30 C250 36 520 34 842 26" fill="none" stroke="url(#waveLine)" stroke-width="3"/>
    </svg>

    <div class="photo photo-sliding-door" role="img" aria-label="Timber sliding door open to a living room with an armchair"></div>

    <div class="years-map" role="img" aria-label="Map of Australia"></div>
    <div class="years"><strong>25</strong><span>YEARS</span></div>

    <p class="history">Bremoda was the first company to introduce retractable fly screens in Australia and has been installing fly screen solutions in beautiful homes with stunning views for over 25 years.</p>
  </main>
</body>
</html>
```